TRI Fold FLYER DESIGN

We would like a Tri Fold Flyer that represents our unique business. Needs to flow. By this I mean the way the flyer folds out the messages need to flow correctly into the next page, be well balanced. bright and colourful and be very effective at getting our USP across.
I have tried Q lane before and was not happy with the outcome hence again sceptical about going down this similar path.
I have attached some of the content in the two screen shots.
Also check out the website to get a further understanding of our unique model/ concept and appearance/ theme.

With a combined 30+ years of experience in their professional back grounds Morris and Dylan have extracted the best practices and methodology and have developed a revolutionary training system that is designed to deliver maximum results in minimum time.

```html
<!DOCTYPE html>
<html lang="en">
<head>
<meta charset="utf-8">
<title>KVT Tri Fold Flyer</title>
<link rel="stylesheet" href="https://fonts.googleapis.com/css2?family=Bebas+Neue&display=swap">
<style>
  :root {
    --page: #ffffff;
    --sky: #a9c3db;
    --steel: #7097bb;
    --sand: #e6cf8c;
    --sun: #f2e51c;
    --ink: #333333;
    --stone: #b8b8b8;
    --shadow: #3a3a3a;
    --white: #ffffff;
    --black: #111111;
  }
  html, body {
    margin: 0;
    padding: 0;
    width: 1200px;
    height: 950px;
    overflow: hidden;
    background: var(--page);
  }
  .flyer {
    position: relative;
    width: 1200px;
    height: 950px;
    overflow: hidden;
    font-family: "Bebas Neue", "Arial Narrow", sans-serif;
    color: var(--white);
  }
  .flyer__header {
    position: absolute;
    left: 0;
    top: 0;
  }
  .flyer__body {
    position: absolute;
    left: 50px;
    top: 240px;
    width: 1100px;
    height: 505px;
    background: var(--steel);
  }
  .flyer__footer {
    position: absolute;
    left: 50px;
    top: 745px;
    width: 1100px;
    height: 140px;
    background: var(--stone);
  }
  .flyer__base {
    position: absolute;
    left: 50px;
    top: 885px;
    width: 1100px;
    height: 14px;
    background: var(--shadow);
  }
  .headline {
    position: absolute;
    left: 66px;
    top: 334px;
    margin: 0;
    font-size: 44px;
    line-height: 35px;
    font-weight: 400;
    letter-spacing: 0.3px;
  }
  .teaser {
    position: absolute;
    left: 130px;
    top: 618px;
    margin: 0;
    font-size: 64px;
    line-height: 64px;
    font-weight: 400;
  }
  .read-on {
    position: absolute;
    left: 142px;
    top: 782px;
    margin: 0;
    font-size: 60px;
    line-height: 60px;
    font-weight: 400;
  }
  .info {
    position: absolute;
    left: 800px;
    width: 340px;
    margin: 0;
  }
  .info__title {
    margin: 0;
    font-size: 29px;
    line-height: 28px;
    font-weight: 400;
  }
  .info__list {
    margin: 0;
    padding: 0;
    list-style: none;
  }
  .info--what { top: 250px; }
  .info--what .info__list li {
    font-size: 21px;
    line-height: 25px;
  }
  .info--why { top: 395px; left: 796px; }
  .info--why .info__list { margin-top: 28px; }
  .info--why .info__list li {
    font-size: 22px;
    line-height: 25px;
  }
  .divider {
    position: absolute;
    left: 795px;
    width: 338px;
    height: 3px;
    border-top: 3px solid var(--ink);
    border-bottom: 3px solid var(--ink);
  }
  .divider--first { top: 377px; }
  .divider--second { top: 597px; }
  .claim {
    position: absolute;
    left: 801px;
    top: 612px;
    margin: 0;
    font-size: 31px;
    line-height: 32px;
    font-weight: 400;
  }
  .question {
    position: absolute;
    left: 825px;
    top: 768px;
    margin: 0;
    font-size: 27px;
    line-height: 28px;
    font-weight: 400;
    color: var(--black);
  }
  .answer {
    position: absolute;
    left: 862px;
    top: 800px;
    margin: 0;
    font-size: 48px;
    line-height: 48px;
    font-weight: 400;
    color: var(--black);
  }
</style>
</head>
<body>
<main class="flyer">
  <svg class="flyer__header" width="1200" height="245" viewBox="0 0 1200 245" aria-hidden="true">
    <rect x="50" y="50" width="1100" height="195" fill="var(--sky)"/>
    <path d="M50 50 H1150 V125 C1080 140 1020 185 960 180 C880 175 800 90 735 92 C650 95 560 175 470 172 C380 168 300 98 230 96 C150 94 90 98 50 98 Z" fill="var(--sand)"/>
    <path d="M50 108 C90 108 150 104 230 106 C300 108 380 178 470 182 C560 185 650 105 735 102 C800 100 880 185 960 190 C1020 195 1080 150 1150 135" fill="none" stroke="var(--sun)" stroke-width="12"/>
    <path d="M50 98 C90 98 150 94 230 96 C300 98 380 168 470 172 C560 175 650 95 735 92 C800 90 880 175 960 180 C1020 185 1080 140 1150 125" fill="none" stroke="var(--ink)" stroke-width="9"/>
    <g class="frame-circles" fill="var(--white)" stroke="var(--ink)" stroke-width="6">
      <circle cx="110" cy="68" r="106"/>
      <circle cx="355" cy="125" r="108"/>
      <circle cx="600" cy="98" r="108"/>
      <circle cx="860" cy="104" r="108"/>
      <circle cx="1110" cy="132" r="108"/>
    </g>
  </svg>

  <div class="flyer__body"></div>
  <div class="flyer__footer"></div>
  <div class="flyer__base"></div>

  <h1 class="headline">What if&nbsp; you could<br>have a gym<br>membership and a<br>personal trainer<br>all rolled into<br>one?</h1>
  <p class="teaser">Curious?</p>
  <p class="read-on">Read on</p>

  <section class="info info--what">
    <h2 class="info__title">What we do:</h2>
    <ul class="info__list">
      <li>• High tempo task oriented functional training</li>
      <li>• Get you in and out the door in 31 minutes</li>
    </ul>
  </section>
  <div class="divider divider--first"></div>

  <section class="info info--why">
    <h2 class="info__title">Why are we different?</h2>
    <ul class="info__list">
      <li>• No booking required</li>
      <li>• Trainer with you all the way</li>
      <li>• No mirrors, no machines</li>
      <li>• No boring treadmills</li>
      <li>• No bull$#!t</li>
      <li>• Just results</li>
    </ul>
  </section>
  <div class="divider divider--second"></div>

  <p class="claim">KVT is the only 31-minute<br>workout with a trainer;<br>results proven and<br>guaranteed</p>

  <p class="question">Will it change your body?</p>
  <p class="answer">Absolutely!!</p>
</main>
</body>
</html>
```